12 Week Weight Loss Program & weight loss challenge postcard/flyer

I want a a5 postcard/flyer design back and front, for my weight loss program. It should be bright and eye catching. The program is done independently from home and has 3 phases, so i would like the back to be split into 3 sections as this can explain the 3 phases. It should have my contact details, instagram account and website address. I also want to include a challenge info on the front, where the person will make £10 for every 10lb lost, depending on them signing up by 1st october. Details about my program can be found on www.sunrisekettlefit.com and on my instagram fresh_path_f1t_ I have attached some pictures of myself training, these dont have to be included if you think its better to not include them, but i would like to see some ideas with them. Also included a copy of the old design, which I don't think was very clear to the audience, so i need it to be clear of what the program entails.
Target Market(s)
females between ages 23-45 who want to lose weight
Industry/Entity Type
Fitness
Requirements
Must have
- must be back and front design
- contact details, email, instagram
- weight loss challenge on the front
- 3 phases explained on the back
- contents of program pack
- benefits of program
- logo
Nice to have
- pictures of myself, not really necessary
- QR code
Should not have
- nudity, men

```html
<!DOCTYPE html>
<html lang="en">
<head>
<meta charset="utf-8">
<title>Sunrise Kettle Fit – 12 Week Weightloss Flyer</title>
<link rel="stylesheet" href="https://fonts.googleapis.com/css2?family=Bebas+Neue&family=Oswald:wght@700&family=Arimo:wght@400&display=swap">
<style>
  :root{
    --page:#e7e5e2;
    --white:#ffffff;
    --ink:#333333;
    --ink-soft:#555555;
    --red:#c9412f;
    --red-band:#cd6457;
    --red-badge:#d8322a;
    --grey-band:#dcdcdc;
    --grey-panel:#f0f0f0;
    --footer:#5b5b5b;
    --divider:#e2e2e2;
  }
  *{box-sizing:border-box;margin:0;padding:0}
  html,body{width:941px;height:1200px;overflow:hidden}
  body{background:var(--page);position:relative;font-family:"Arimo",Arial,sans-serif}
  ul{list-style:none}

  /* ---------- front card ---------- */
  .card-front{position:absolute;left:89px;top:79px;width:673px;height:474px;background:var(--white);overflow:hidden}
  .card-front__art{position:absolute;inset:0}
  .front__kicker{position:absolute;left:20px;top:24px;font-family:"Bebas Neue",sans-serif;font-size:20px;color:var(--red);letter-spacing:.2px;white-space:nowrap}
  .front__title{position:absolute;left:27px;top:64px;font-family:"Oswald",sans-serif;font-weight:700;font-size:80px;line-height:64px;color:var(--ink);letter-spacing:-1px;transform:scaleX(.92);transform-origin:left top}
  .benefits{position:absolute;left:23px;top:222px}
  .benefits li{position:relative;padding-left:20px;font-family:"Bebas Neue",sans-serif;font-size:24px;line-height:25px;color:var(--ink)}
  .bullet::before{content:"";position:absolute;left:0;top:50%;width:11px;height:11px;margin-top:-7px;border:1px solid var(--red);border-radius:50%}
  .bullet::after{content:"";position:absolute;left:3px;top:50%;width:3px;height:3px;margin-top:-4px;border-top:1px solid var(--red);border-right:1px solid var(--red);transform:rotate(45deg)}
  .challenge{position:absolute;left:0;top:341px;width:293px;height:58px;background:var(--red-band);color:var(--white);font-family:"Bebas Neue",sans-serif;font-size:23px;line-height:23px;text-align:center;padding-top:6px}
  .web-strip{position:absolute;left:0;top:399px;width:293px;height:75px;background:var(--grey-band)}
  .web-strip__url{position:absolute;left:29px;top:27px;font-family:"Bebas Neue",sans-serif;font-size:24px;color:var(--red);white-space:nowrap}
  .brand-mark{position:absolute;left:305px;top:428px;font-family:"Bebas Neue",sans-serif;font-size:26px;color:var(--white);white-space:nowrap}
  .badge{position:absolute;left:524px;top:305px;width:130px;height:130px;border-radius:50%;background:var(--white);padding:5px}
  .badge__inner{width:100%;height:100%;border-radius:50%;background:var(--red-badge);color:var(--white);font-family:"Bebas Neue",sans-serif;font-size:24px;line-height:23px;text-align:center;padding-top:37px}

  /* ---------- back card ---------- */
  .card-back{position:absolute;left:182px;top:602px;width:672px;height:475px;background:var(--grey-panel);overflow:hidden}
  .card-back__header{position:absolute;inset:0 0 auto 0;height:110px}
  .back__title{position:absolute;left:0;right:0;top:22px;text-align:center;font-family:"Bebas Neue",sans-serif;font-size:58px;line-height:58px;color:var(--white);letter-spacing:.5px}
  .phase{position:absolute;top:0;height:294px;background:var(--white);padding:127px 0 0 26px}
  .phase--1{left:0;width:217px}
  .phase--2{left:224px;width:208px;padding-left:22px}
  .phase--3{left:440px;width:232px;padding-left:22px}
  .phase__heading{font-family:"Bebas Neue",sans-serif;font-size:18px;line-height:18px;color:var(--red);margin-bottom:11px}
  .phase__list li{position:relative;padding-left:16px;font-size:12px;line-height:23.6px;color:var(--ink-soft);text-transform:uppercase}
  .phase__list .bullet::before{width:9px;height:9px;margin-top:-5px}
  .phase__list .bullet::after{left:2px;margin-top:-2.5px;width:2.5px;height:2.5px}
  .phase--3 .phase__list{margin-top:-1px}
  .about{position:absolute;left:40px;right:40px;top:321px;text-align:center;font-size:12px;line-height:16px;color:var(--ink-soft)}
  .about__note{margin-top:15px}
  .about__cta{color:var(--red);text-transform:uppercase}
  .contact-bar{position:absolute;left:0;right:0;bottom:0;height:36px;background:var(--footer);color:var(--white);font-size:13px;text-transform:uppercase}
  .contact-bar__item{position:absolute;top:0;height:36px;display:flex;align-items:center;gap:8px;white-space:nowrap}
  .contact-bar__item--social{left:22px}
  .contact-bar__item--web{left:163px;gap:12px}
  .contact-bar__item--mail{left:424px;gap:10px}
  .social-square{width:14px;height:14px;border:2px solid var(--white);border-radius:3px}
</style>
</head>
<body>

<section class="card-front" aria-label="Flyer front">
  <svg class="card-front__art" width="673" height="474" viewBox="0 0 673 474" aria-hidden="false">
    <defs>
      <linearGradient id="photoTone" x1="0" y1="0" x2="0.6" y2="1">
        <stop offset="0" stop-color="#b9c4c6"/>
        <stop offset="0.45" stop-color="#7d8b93"/>
        <stop offset="1" stop-color="#4e5a66"/>
      </linearGradient>
    </defs>
    <polygon points="347,0 355,0 280,474 272,474" fill="#d9d9d9"/>
    <polygon points="355,0 400,0 290,474 278,474" fill="var(--red)"/>
    <polygon points="400,0 673,0 673,474 290,474" fill="url(#photoTone)" role="img" aria-label="Photo of the trainer in workout wear, hands behind head, in a home gym"/>
  </svg>

  <p class="front__kicker">Sunrise Kettle Fit / / 12 Week Weightloss</p>
  <h1 class="front__title">TRAINING<br>PROGRAM</h1>
  <ul class="benefits">
    <li class="bullet">Detox</li>
    <li class="bullet">Boost Metabolism</li>
    <li class="bullet">Reduce Body Fat</li>
    <li class="bullet">Buold Muscle &amp; Increase Fitness</li>
  </ul>
  <p class="challenge">Signing up by 1st October<br>&amp; get £10 for every 10lb lost</p>
  <div class="web-strip"><p class="web-strip__url">www.sunrisekettlefit.com</p></div>
  <p class="brand-mark">Sunrise Kettle Fit</p>
  <div class="badge"><p class="badge__inner">Home Based<br>Training</p></div>
</section>

<section class="card-back" aria-label="Flyer back">
  <article class="phase phase--1">
    <h3 class="phase__heading">Phase 1<br>Cleanse &amp; Boost Metabolism</h3>
    <ul class="phase__list">
      <li class="bullet">10 Day Detox</li>
      <li class="bullet">Resistance Training</li>
      <li class="bullet">Meal Planing</li>
      <li class="bullet">No Cardio</li>
      <li class="bullet">Supplements</li>
    </ul>
  </article>
  <article class="phase phase--2">
    <h3 class="phase__heading">Phase 2<br>Reduce Body Fat Build Muscle</h3>
    <ul class="phase__list">
      <li class="bullet">Resistance Training</li>
      <li class="bullet">Meal Planing</li>
      <li class="bullet">No Cardio</li>
      <li class="bullet">Supplements</li>
    </ul>
  </article>
  <article class="phase phase--3">
    <h3 class="phase__heading">Phase 3<br>Burn Body Fat Build Muscle<br>Increase Fitness</h3>
    <ul class="phase__list">
      <li class="bullet">Resistance Training</li>
      <li class="bullet">Plyometrics</li>
      <li class="bullet">Meal Planing</li>
      <li class="bullet">Supplements</li>
    </ul>
  </article>

  <svg class="card-back__header" width="672" height="110" viewBox="0 0 672 110" aria-hidden="true">
    <polygon points="0,67 336,104 672,67 672,80 336,110 0,80" fill="#d6d6d6"/>
    <polygon points="0,0 672,0 672,69 336,102 0,69" fill="var(--red-band)"/>
  </svg>
  <h2 class="back__title">4 Week Phases</h2>

  <div class="about">
    <p>This progra is fully home based, gym’s optional. The program will consist of a shopping list or all supplements, detox, workout &amp; meal program for the duration of 12 weeks, including full support &amp; instructional videos, with an option of one-on-one personal training sessions in your preferres location.</p>
    <p class="about__note">If you have any medical conditions, please ensure you consult your GP before takin part.</p>
    <p class="about__cta">For more information or to book on the program please call 07700900123 or email.</p>
  </div>

  <footer class="contact-bar">
    <div class="contact-bar__item contact-bar__item--social"><span class="social-square"></span>fresh_path_f1t_</div>
    <div class="contact-bar__item contact-bar__item--web">
      <svg width="16" height="16" viewBox="0 0 16 16" aria-hidden="true" fill="none" stroke="#fff" stroke-width="1.1">
        <circle cx="8" cy="8" r="7"/><ellipse cx="8" cy="8" rx="3" ry="7"/><line x1="1" y1="8" x2="15" y2="8"/><line x1="2" y1="4.5" x2="14" y2="4.5"/><line x1="2" y1="11.5" x2="14" y2="11.5"/>
      </svg>www.sunrisekettlefit.com</div>
    <div class="contact-bar__item contact-bar__item--mail">
      <svg width="18" height="15" viewBox="0 0 18 15" aria-hidden="true" fill="none" stroke="#fff" stroke-width="1.3">
        <path d="M1 6 L9 1 L17 6 V14 H1 Z"/><path d="M1 6 L9 11 L17 6"/>
      </svg>hello@sunrisekettlefit.com</div>
  </footer>
</section>

</body>
</html>
```